Website for a new investor-focused estate agency portal

Require a website for a new investor-focused estate agency portal, this will interface with our exisitng API for data posting and retrieval. We have a logo for the business, but will happily change the colour palette to suit the design.
Requirements:
1) Landing page to describe the business
- Feature line showing the latest properties in our listings
- Announcement section (e.g. mobile app coming soon)
- Text area - what we do for Investors
- Text area - what we do for Agents and sourcers
- Text area - what we do for Home buyers
- Small Q&A
- Subscription pricing description and sign up
2) Content page (product updates page)
A timeline to list list releases, new features and other improvements to the service, website and app, shown in most recent date order.
3) A property search/result page including search form
4) A single property detail page, including
- carousel for images and video
- map
- text content
5) A data entry page to enter property data into the system. This page will contain a sidebar menu, property name, address, description, and about 10 other fields (detail to be provided). The attached screen dump files are snapshot of the wireframe form used by the development team for the property entry page.
Target Market(s)
Property investors / Real estate buyer's including personal home buyers.
Number of Pages Required
5+ page
Colors
Designer to choose colors to be used in the design.
Requirements
Must have
- Clean, crisp design and presentaion.
Nice to have
- The Search/result page (3) and the detail page (4) may have 2-3 elements for paid advertising but should also look good without those elements.
Should not have
- Must not be too busy with distracting elements

```html
<!DOCTYPE html>
<html lang="en">
<head>
<meta charset="utf-8">
<title>Homestead Hub — Find Your Dream Home</title>
<link href="https://fonts.googleapis.com/css2?family=Roboto:wght@300;400;500;700;900&display=swap" rel="stylesheet">
<style>
:root{
  --purple:#2e2178;
  --purple-mid:#3a2b8e;
  --purple-deep:#251a63;
  --ink:#1d1d2b;
  --text:#444450;
  --muted:#777784;
  --line:#d9d9e2;
  --white:#ffffff;
  --footer:#0b0b0d;
  --grey-card:#4b4b4f;
}
*{box-sizing:border-box;margin:0;padding:0}
html,body{width:1200px;height:4894px;overflow:hidden}
body{font-family:"Roboto",Arial,sans-serif;color:var(--text);background:var(--white);position:relative}
section,header,footer{position:absolute;left:0;width:1200px;overflow:hidden}
.btn{position:absolute;display:flex;align-items:center;justify-content:center;font-weight:700;font-size:14px;letter-spacing:.3px;text-transform:uppercase}
.btn-solid{background:var(--purple);color:var(--white)}
.btn-ghost{border:2px solid var(--white);color:var(--white)}
.btn-outline{border:2px solid var(--purple);color:var(--purple);background:var(--white)}

/* header */
.site-header{top:0;height:86px;background:var(--white);border-bottom:1px solid #eee}
.brand{position:absolute;left:130px;top:26px;display:flex;align-items:center;gap:12px;font-weight:900;font-size:23px;color:var(--purple);letter-spacing:.3px}
.brand-dot{width:28px;height:28px;background:var(--purple)}
.main-nav{position:absolute;left:434px;top:36px;display:flex;gap:32px;font-size:15px;color:#777}
.main-nav .active{color:var(--ink);font-weight:500}

/* hero */
.hero{top:86px;height:645px}
.hero-photo{position:absolute;inset:0;background:linear-gradient(180deg,#f4c9b6 0%,#e8b7a8 30%,#b8b6c6 48%,#8a8f86 62%,#5f7b3f 78%,#4a6a2f 100%)}
.hero-house{position:absolute;left:560px;top:0;width:640px;height:560px;background:linear-gradient(160deg,#8c6a56 0%,#c8b8a8 40%,#f2ede4 60%,#9a8f86 100%);opacity:.75}
.hero-copy{position:absolute;left:100px;width:530px;top:175px;text-align:center;color:var(--purple-deep)}
.hero-welcome{font-size:27px;font-weight:400;letter-spacing:1px}
.hero-title{font-size:42px;font-weight:900;margin-top:10px;line-height:1}
.hero-sub{font-size:35px;font-weight:900;margin-top:8px;line-height:1}
.hero .btn{left:266px;top:351px;width:198px;height:46px}
.hero-dots{position:absolute;left:570px;top:596px;display:flex;gap:8px}
.hero-dots span{width:11px;height:11px;border-radius:50%;background:var(--white);border:1px solid rgba(0,0,0,.2)}
.hero-dots span:first-child{background:transparent;border:2px solid var(--white)}
.hero-cut{position:absolute;left:0;bottom:0}

/* featured */
.featured{top:731px;height:599px;background:#f7f7f8}
.featured-bg{position:absolute;inset:0;background:linear-gradient(90deg,#c9c9cc 0%,#ececee 18%,#f8f8f9 40%,#f8f8f9 60%,#ececee 82%,#c2c2c6 100%)}
.section-title{position:absolute;left:0;width:1200px;text-align:center;font-weight:700;color:var(--purple);text-transform:uppercase}
.featured .section-title{top:86px;font-size:27px}
.prop-card{position:absolute;top:147px;width:285px;height:367px;background:var(--white);border:1px solid #ddd;box-shadow:0 2px 8px rgba(0,0,0,.08)}
.prop-photo{height:184px}
.prop-body{padding:18px 26px 0}
.prop-title{font-size:21px;color:var(--ink);font-weight:400}
.prop-addr{font-size:13px;color:var(--muted);margin-top:6px}
.prop-meta{display:flex;gap:18px;margin-top:16px;font-size:12px;color:var(--muted);align-items:center}
.prop-meta span{display:flex;align-items:center;gap:8px}
.prop-card .btn{left:26px;top:311px;width:137px;height:34px;font-size:12px}
.carousel-arrow{position:absolute;top:300px}

/* app */
.app{top:1330px;height:479px;background:var(--purple)}
.app-skyline{position:absolute;left:0;right:0;bottom:0;height:300px;background:linear-gradient(180deg,rgba(255,255,255,0) 0%,rgba(255,255,255,.06) 100%)}
.phone{position:absolute;left:224px;top:49px;width:274px;height:460px;border-radius:40px;background:#f1f1f4;border:6px solid #d8d8de}
.phone-speaker{position:absolute;left:110px;top:18px;width:42px;height:5px;border-radius:3px;background:#ccc}
.phone-name{position:absolute;left:0;width:262px;top:165px;text-align:center;font-size:30px;font-weight:700;color:var(--purple);line-height:1.25}
.app-copy{position:absolute;left:598px;top:116px;color:var(--white);width:460px}
.app-kicker{font-size:30px;font-weight:500}
.app-title{font-size:38px;font-weight:700;margin-top:6px}
.app-copy p{font-size:14px;line-height:27px;margin-top:18px;opacity:.92}
.app .btn{left:602px;top:321px;width:181px;height:49px}

/* investors */
.investors{top:1809px;height:581px;background:linear-gradient(180deg,#ffffff 0%,#f1f1f3 100%)}
.kicker{position:absolute;left:0;width:1200px;text-align:center;color:var(--purple);font-weight:500}
.investors .kicker{top:100px;font-size:21px}
.investors .section-title{top:128px;font-size:29px}
.lead{position:absolute;text-align:center;font-size:16px;line-height:27px;color:var(--text)}
.investors .lead{left:320px;width:560px;top:168px}
.service{position:absolute;top:287px;width:212px;height:194px;background:var(--white);border:2px solid #aaa3cc;text-align:center}
.service-icon{position:absolute;left:78px;top:-38px;width:56px;height:56px;background:var(--purple);transform:rotate(45deg)}
.service-icon svg{transform:rotate(-45deg)}
.service h3{margin-top:54px;font-size:17px;color:var(--purple);font-weight:500}
.service p{font-size:10px;line-height:15px;color:var(--muted);margin:12px 20px 0}
.service .btn{left:45px;top:146px;width:122px;height:28px;font-size:10px}

/* agents */
.agents{top:2390px;height:479px}
.agents-photo{position:absolute;inset:0;background:linear-gradient(100deg,#2d2d33 0%,#4a4a52 35%,#6b6b73 55%,#3c3c44 80%,#2a2a30 100%)}
.agents .kicker{top:108px;font-size:26px;color:var(--white);font-weight:400}
.agents .section-title{top:140px;font-size:36px;color:var(--white);font-weight:500}
.agents .lead{left:246px;width:704px;top:196px;color:var(--white);font-size:18px;line-height:28px}
.agents .btn{left:505px;top:304px;width:173px;height:50px}

/* home buyers */
.buyers{top:2869px;height:500px;background:var(--white)}
.buyers-photo{position:absolute;left:551px;top:0;width:649px;height:500px;background:linear-gradient(90deg,#ffffff 0%,#eeeef1 25%,#d4d0e6 55%,#8a7fc7 75%,#c5a891 100%)}
.left-copy{position:absolute;left:160px}
.buyers .left-copy{top:113px}
.left-kicker{font-size:21px;color:var(--purple);font-weight:500}
.left-title{font-size:29px;color:var(--purple);font-weight:700;text-transform:uppercase;margin-top:2px}
.left-copy p{font-size:16px;line-height:27px;margin-top:14px;width:410px}
.buyers .btn{left:162px;top:327px;width:169px;height:44px}

/* faq */
.faq{top:3369px;height:589px;background:var(--purple-mid)}
.faq .section-title{top:86px;color:var(--white);font-size:29px;font-weight:500}
.faq-item{position:absolute;left:224px;width:764px;border:1px solid rgba(255,255,255,.55);color:var(--white);padding:0 22px}
.faq-q{font-size:17px;font-weight:500;line-height:54px;display:flex;justify-content:space-between}
.faq-item.open .faq-q{line-height:36px}
.faq-a{font-size:13px;line-height:17px;opacity:.9;padding-bottom:12px}
.faq-sign{font-size:26px;font-weight:300}

/* pricing */
.pricing{top:3958px;height:532px;background:var(--white)}
.pricing-bg{position:absolute;inset:0;background:linear-gradient(90deg,#d2d2d6 0%,#f1f1f3 30%,#ffffff 50%,#eeeef0 80%,#d5d5d8 100%)}
.pricing .left-copy{top:124px}
.pricing .left-title{font-size:29px;line-height:34px}
.pricing .left-copy p{width:310px}
.pricing .btn{left:156px;top:311px;width:167px;height:44px}
.plan{position:absolute;top:45px;width:250px;height:399px;background:var(--white);box-shadow:0 3px 12px rgba(0,0,0,.12);text-align:center}
.plan-head{position:relative;height:150px;color:var(--white)}
.plan-name{padding-top:26px;font-size:20px;font-weight:300;letter-spacing:.5px}
.plan-price{font-size:30px;font-weight:700;margin-top:4px}
.plan-price small{font-size:15px;font-weight:400}
.plan-price sup{font-size:16px;font-weight:400;vertical-align:10px}
.plan-wave{position:absolute;left:0;bottom:-1px}
.plan ul{list-style:none;text-align:left;margin:16px 0 0 28px;font-size:11px;line-height:14px;color:var(--muted)}
.plan li{display:flex;gap:7px;margin-bottom:16px;width:196px}
.plan .btn{left:26px;top:339px;width:198px;height:40px;font-size:14px}

/* footer */
.site-footer{top:4480px;height:414px;background:transparent}
.footer-peak{position:absolute;left:0;top:0}
.footer-body{position:absolute;left:0;top:60px;width:1200px;height:354px;background:var(--footer)}
.footer-col{position:absolute;top:48px;color:#d8d8dc;font-size:13px}
.footer-col h4{color:var(--white);font-size:17px;font-weight:500;margin-bottom:14px;letter-spacing:.3px}
.footer-col ul{list-style:none;line-height:23px}
.contact-row{display:flex;gap:12px;margin-bottom:14px;line-height:16px}
.ico{width:28px;height:28px;border-radius:50%;background:var(--white);flex:none;display:flex;align-items:center;justify-content:center}
.nl-input{margin-top:12px;width:224px;height:33px;background:var(--white);color:#555;font-size:10px;padding:0 11px;display:flex;align-items:center}
.nl-btn{margin-top:13px;width:118px;height:32px;background:var(--purple-mid);color:var(--white);font-size:13px;font-weight:700;display:flex;align-items:center;justify-content:center}
.social small{display:block;font-size:10px;color:#aaa}
.footer-rule{position:absolute;left:0;top:288px;width:1200px;height:1px;background:#2a2a2e}
.copyright{position:absolute;left:0;top:316px;width:1200px;text-align:center;font-size:13px;color:#9a9aa0}
</style>
</head>
<body>

<header class="site-header">
  <div class="brand"><span class="brand-dot"></span>HOMESTEAD HUB</div>
  <nav class="main-nav">
    <span class="active">ABOUT US</span><span>PROPERTY</span><span>INVESTORS</span><span>HOME BUYERS</span><span>PRICING</span><span>CONTACT US</span>
  </nav>
</header>

<section class="hero">
  <div class="hero-photo" role="img" aria-label="Seaside timber house with white veranda and green lawn at sunset"></div>
  <div class="hero-house" aria-hidden="true"></div>
  <div class="hero-copy">
    <div class="hero-welcome">— WELCOME TO—</div>
    <div class="hero-title">FIND YOUR DREAM HOME</div>
    <div class="hero-sub">WITH HOMESTEAD HUB</div>
  </div>
  <a class="btn btn-solid">Get Started Now</a>
  <div class="hero-dots"><span></span><span></span><span></span><span></span></div>
  <svg class="hero-cut" width="1200" height="120" viewBox="0 0 1200 120">
    <polygon points="0,18 600,108 1200,18 1200,120 0,120" fill="#f7f7f8"/>
    <polyline points="0,10 600,100 1200,10" fill="none" stroke="#2e2178" stroke-width="7"/>
  </svg>
</section>

<section class="featured">
  <div class="featured-bg" role="img" aria-label="Faded suburban houses in the background"></div>
  <h2 class="section-title">Featured Properties</h2>
  <svg class="carousel-arrow" style="left:92px" width="26" height="56" viewBox="0 0 26 56"><polyline points="24,2 2,28 24,54" fill="none" stroke="#666" stroke-width="2"/></svg>
  <svg class="carousel-arrow" style="left:1084px" width="26" height="56" viewBox="0 0 26 56"><polyline points="2,2 24,28 2,54" fill="none" stroke="#666" stroke-width="2"/></svg>

  <article class="prop-card" style="left:146px">
    <div class="prop-photo" role="img" aria-label="Two-storey modern family house" style="background:linear-gradient(180deg,#8fb2d8 0%,#c9b89a 55%,#6e7b4c 100%)"></div>
    <div class="prop-body">
      <div class="prop-title">Property Title here</div>
      <div class="prop-addr">48 Larkfield Row #B Austin</div>
      <div class="prop-meta">
        <span><svg width="22" height="14" viewBox="0 0 22 14"><rect x="1" y="5" width="20" height="6" fill="none" stroke="#888"/><rect x="1" y="1" width="6" height="4" fill="none" stroke="#888"/><line x1="1" y1="11" x2="1" y2="14" stroke="#888"/><line x1="21" y1="11" x2="21" y2="14" stroke="#888"/></svg>03 Bedroom</span>
        <span><svg width="22" height="14" viewBox="0 0 22 14"><path d="M1 6h20v3a4 4 0 0 1-4 4H5a4 4 0 0 1-4-4z" fill="none" stroke="#888"/><path d="M16 6V2h3" fill="none" stroke="#888"/></svg>02 Bathroom</span>
      </div>
    </div>
    <a class="btn btn-solid">View Details</a>
  </article>

  <article class="prop-card" style="left:458px">
    <div class="prop-photo" role="img" aria-label="Contemporary house with lit windows at dusk" style="background:linear-gradient(180deg,#9aa3ad 0%,#e4ddd2 45%,#4a4a4e 100%)"></div>
    <div class="prop-body">
      <div class="prop-title">Property Title here</div>
      <div class="prop-addr">48 Larkfield Row #B Austin</div>
      <div class="prop-meta">
        <span><svg width="22" height="14" viewBox="0 0 22 14"><rect x="1" y="5" width="20" height="6" fill="none" stroke="#888"/><rect x="1" y="1" width="6" height="4" fill="none" stroke="#888"/><line x1="1" y1="11" x2="1" y2="14" stroke="#888"/><line x1="21" y1="11" x2="21" y2="14" stroke="#888"/></svg>03 Bedroom</span>
        <span><svg width="22" height="14" viewBox="0 0 22 14"><path d="M1 6h20v3a4 4 0 0 1-4 4H5a4 4 0 0 1-4-4z" fill="none" stroke="#888"/><path d="M16 6V2h3" fill="none" stroke="#888"/></svg>02 Bathroom</span>
      </div>
    </div>
    <a class="btn btn-solid">View Details</a>
  </article>

  <article class="prop-card" style="left:775px">
    <div class="prop-photo" role="img" aria-label="Single-storey home with garden under blue sky" style="background:linear-gradient(180deg,#4d8fd0 0%,#a9c6e2 40%,#7b8a6a 65%,#3f6a2c 100%)"></div>
    <div class="prop-body">
      <div class="prop-title">Property Title here</div>
      <div class="prop-addr">48 Larkfield Row #B Austin</div>
      <div class="prop-meta">
        <span><svg width="22" height="14" viewBox="0 0 22 14"><rect x="1" y="5" width="20" height="6" fill="none" stroke="#888"/><rect x="1" y="1" width="6" height="4" fill="none" stroke="#888"/><line x1="1" y1="11" x2="1" y2="14" stroke="#888"/><line x1="21" y1="11" x2="21" y2="14" stroke="#888"/></svg>03 Bedroom</span>
        <span><svg width="22" height="14" viewBox="0 0 22 14"><path d="M1 6h20v3a4 4 0 0 1-4 4H5a4 4 0 0 1-4-4z" fill="none" stroke="#888"/><path d="M16 6V2h3" fill="none" stroke="#888"/></svg>02 Bathroom</span>
      </div>
    </div>
    <a class="btn btn-solid">View Details</a>
  </article>
</section>

<section class="app">
  <div class="app-skyline" role="img" aria-label="Faint city skyline silhouette"></div>
  <div class="phone">
    <div class="phone-speaker"></div>
    <div class="phone-name">HOMESTEAD<br>HUB</div>
  </div>
  <div class="app-copy">
    <div class="app-kicker">MOBILE APP</div>
    <div class="app-title">COMING SOON</div>
    <p>Maecenas aliquet velit vel turpis Mauris neque metus malesuada nec ultricies sit amet porttitor mattis enim In massa libero inter-dum nec interdum vel blandit sed nulla In ullamco</p>
  </div>
  <a class="btn btn-ghost">Learn More</a>
</section>

<section class="investors">
  <div class="kicker">WHAT WE DO</div>
  <h2 class="section-title">For Investors</h2>
  <p class="lead">Maecenas aliquet velit vel turpis Mauris neque metus malesuada nec ultricies sit amet porttitor mattis enim In massa</p>

  <div class="service" style="left:124px">
    <div class="service-icon"><svg width="56" height="56" viewBox="0 0 56 56"><path d="M28 40V22M28 30c-6 0-9-4-9-8 5 0 9 3 9 8zM28 27c6 0 9-4 9-8-5 0-9 3-9 8z" fill="none" stroke="#fff" stroke-width="2"/></svg></div>
    <h3>Service Heading</h3>
    <p>Maecenas aliquet velit vel turpis Mauris neque metus malesuada nec ultricies sit amet</p>
    <a class="btn btn-solid">Learn More</a>
  </div>
  <div class="service" style="left:361px">
    <div class="service-icon"><svg width="56" height="56" viewBox="0 0 56 56"><circle cx="28" cy="25" r="8" fill="none" stroke="#fff" stroke-width="2"/><path d="M24 33h8M25 37h6" stroke="#fff" stroke-width="2"/></svg></div>
    <h3>Service Heading</h3>
    <p>Maecenas aliquet velit vel turpis Mauris neque metus malesuada nec ultricies sit amet</p>
    <a class="btn btn-solid">Learn More</a>
  </div>
  <div class="service" style="left:598px">
    <div class="service-icon"><svg width="56" height="56" viewBox="0 0 56 56"><path d="M16 27l7-6 6 3 5-3 7 6-9 8z" fill="none" stroke="#fff" stroke-width="2" stroke-linejoin="round"/></svg></div>
    <h3>Service Heading</h3>
    <p>Maecenas aliquet velit vel turpis Mauris neque metus malesuada nec ultricies sit amet</p>
    <a class="btn btn-solid">Learn More</a>
  </div>
  <div class="service" style="left:836px">
    <div class="service-icon"><svg width="56" height="56" viewBox="0 0 56 56"><circle cx="28" cy="29" r="9" fill="none" stroke="#fff" stroke-width="2"/><path d="M24 19h8l-2 3h-4z" fill="none" stroke="#fff" stroke-width="2"/></svg></div>
    <h3>Service Heading</h3>
    <p>Maecenas aliquet velit vel turpis Mauris neque metus malesuada nec ultricies sit amet</p>
    <a class="btn btn-solid">Learn More</a>
  </div>
</section>

<section class="agents">
  <div class="agents-photo" role="img" aria-label="Agent showing a couple around a property, darkened"></div>
  <div class="kicker">WHAT WE DO FOR</div>
  <h2 class="section-title">Agents and Sourcers</h2>
  <p class="lead">Mauris neque metus malesuada nec ultricies sit amet porttitor mattis enim In massa libero interdum nec interdum vel blandit sed nulla In ullamcorper est eget tempor cursus neque mi consectetuer mi a ultricies</p>
  <a class="btn btn-ghost">Learn More</a>
</section>

<section class="buyers">
  <div class="buyers-photo" role="img" aria-label="Couple sitting on the floor of a new home with a sketched interior around them"></div>
  <div class="left-copy">
    <div class="left-kicker">WHAT WE DO FOR</div>
    <h2 class="left-title">For Home Buyers</h2>
    <p>Mauris neque metus malesuada nec ultricies sit amet porttitor mattis enim In massa libero interdum nec in-terdum vel blandit sed nulla In ullamcorper est eget tempor cursus neque mi consectetuer</p>
  </div>
  <a class="btn btn-solid">Learn More</a>
</section>

<section class="faq">
  <h2 class="section-title">Question and Answer</h2>
  <div class="faq-item" style="top:142px;height:56px"><div class="faq-q">Nunc tempus felis vitae urna Vivamus porttitor ?<span class="faq-sign">+</span></div></div>
  <div class="faq-item" style="top:207px;height:55px"><div class="faq-q">Phasellus pellentesque aliquam enim Proin dui lectus cursus?<span class="faq-sign">+</span></div></div>
  <div class="faq-item open" style="top:271px;height:109px;padding-top:10px">
    <div class="faq-q">Morbi eget arcu Morbi porta libero ?<span class="faq-sign">−</span></div>
    <div class="faq-a">Pellentesque faucibus Ut accumsan ultricies elit Maecenas at justo id velit placerat molestie Donec dictum lectus non odio Cras a ante vitae enim iaculis aliquam Mauris nunc quam venenatis nec</div>
  </div>
  <div class="faq-item" style="top:387px;height:55px"><div class="faq-q">Fusce tellus Sed metus augue convallis et vehicula?<span class="faq-sign">+</span></div></div>
  <div class="faq-item" style="top:450px;height:53px"><div class="faq-q" style="line-height:52px">Nunc tempus felis vitae urna Vivamus porttitor neque ?<span class="faq-sign">+</span></div></div>
</section>

<section class="pricing">
  <div class="pricing-bg" role="img" aria-label="Faded house exterior in the background"></div>
  <div class="left-copy">
    <h2 class="left-title">Subscription<br>Pricing</h2>
    <p>Maecenas aliquet velit vel turpis Mauris neque metus malesuada nec ultricies sit amet porttitor mattis enim In</p>
  </div>
  <a class="btn btn-solid">Learn More</a>

  <div class="plan" style="left:496px">
    <div class="plan-head" style="background:var(--purple-mid)">
      <div class="plan-name">BASIC</div>
      <div class="plan-price"><sup>$</sup>49.99<small>/mo</small></div>
      <svg class="plan-wave" width="250" height="40" viewBox="0 0 250 40"><path d="M0 20C58 0 100 40 158 22S232 8 250 18V40H0z" fill="#fff"/></svg>
    </div>
    <ul>
      <li><span>✓</span>Sed metus augue convallis et vehicula ut pulvinar eu ante</li>
      <li><span>✓</span>Integer orci tellus tristique vitae consequat nec</li>
      <li><span>✓</span>Aauris viverra in gravida eu</li>
      <li><span>✓</span>Curabitur iaculis tempus eros</li>
    </ul>
    <a class="btn btn-outline">Sign Up Now</a>
  </div>

  <div class="plan" style="left:781px">
    <div class="plan-head" style="background:var(--grey-card)">
      <div class="plan-name">PLATINUM</div>
      <div class="plan-price"><sup>$</sup>89.99<small>/mo</small></div>
      <svg class="plan-wave" width="250" height="40" viewBox="0 0 250 40"><path d="M0 20C58 0 100 40 158 22S232 8 250 18V40H0z" fill="#fff"/></svg>
    </div>
    <ul>
      <li><span>✓</span>Sed metus augue convallis et vehicula ut pulvinar eu ante</li>
      <li><span>✓</span>Integer orci tellus tristique vitae consequat nec</li>
      <li><span>✓</span>Aauris viverra in gravida eu</li>
      <li><span>✓</span>Curabitur iaculis tempus eros</li>
    </ul>
    <a class="btn btn-outline">Sign Up Now</a>
  </div>
</section>

<footer class="site-footer">
  <svg class="footer-peak" width="1200" height="62" viewBox="0 0 1200 62"><polygon points="0,62 600,0 1200,62" fill="#0b0b0d"/></svg>
  <div class="footer-body">
    <div class="footer-col" style="left:179px">
      <h4>MENU</h4>
      <ul><li>About Us</li><li>Properties</li><li>Investors</li><li>Home Buyers</li><li>Pricing</li><li>Contact Us</li></ul>
    </div>
    <div class="footer-col" style="left:352px">
      <h4>CONTACT US</h4>
      <div class="contact-row"><span class="ico"><svg width="12" height="16" viewBox="0 0 12 16"><path d="M6 15S1 9 1 6a5 5 0 0 1 10 0c0 3-5 9-5 9z" fill="#111"/><circle cx="6" cy="6" r="2" fill="#fff"/></svg></span><span>48 Larkfield Row #B<br>Austin 78701 TX</span></div>
      <div class="contact-row"><span class="ico"><svg width="14" height="14" viewBox="0 0 14 14"><path d="M3 1l3 3-2 2a8 8 0 0 0 4 4l2-2 3 3-2 2C6 13 1 8 1 3z" fill="#111"/></svg></span><span>Call Us<br>555.014.2290</span></div>
      <div class="contact-row"><span class="ico"><svg width="14" height="10" viewBox="0 0 14 10"><rect x="0.5" y="0.5" width="13" height="9" fill="none" stroke="#111"/><polyline points="1,1 7,6 13,1" fill="none" stroke="#111"/></svg></span><span>Email Us<br>hello@homesteadhub.example</span></div>
    </div>
    <div class="footer-col" style="left:637px">
      <h4>GET UPDATES</h4>
      <div>Subscribe for Our Newsletters</div>
      <div class="nl-input">ENTER EMAIL ADDRESS</div>
      <div class="nl-btn">SUBSCRIBE</div>
    </div>
    <div class="footer-col social" style="left:927px">
      <h4>GET IN TOUCH</h4>
      <div class="contact-row"><span class="ico"></span><span><small>Like us on</small>Facepage</span></div>
      <div class="contact-row"><span class="ico"></span><span><small>Follow us on</small>Chirper</span></div>
      <div class="contact-row"><span class="ico"></span><span><small>Follow us on</small>Linkwork</span></div>
    </div>
    <div class="footer-rule"></div>
    <div class="copyright">Copyright © 2019 All right reserved</div>
  </div>
</footer>

</body>
</html>
```